National commercial insurance agency needs design for email campaign to other insurance agencies ...

National commercial insurance agency needs design for email campaign to other insurance agencies needing to place workers comp policies and and also need very intense risk management. We want to market to smaller insurance agencies to refer us to their larger clients or prospects.

Font styles to use
Sans Serif

```html
<!DOCTYPE html>
<html lang="en">
<head>
<meta charset="utf-8">
<title>Anchor Cover – Email</title>
<link rel="stylesheet" href="https://fonts.googleapis.com/css2?family=Source+Sans+3:wght@300;400;600;700&display=swap">
<style>
:root{
  --brand:#e8401c;
  --ink:#3a3a3a;
  --muted:#8a8a8a;
  --band:#ececec;
  --white:#ffffff;
  --card-shadow:0 4px 14px rgba(0,0,0,.12);
}
*{box-sizing:border-box;margin:0;padding:0}
html,body{width:1200px;height:4401px;overflow:hidden;background:var(--white)}
body{font-family:"Source Sans 3",Arial,sans-serif;color:var(--ink);position:relative}
.abs{position:absolute}

.topbar{left:0;top:0;width:1200px;height:123px;background:var(--brand)}
.wordmark{color:var(--white);font-weight:700;letter-spacing:1px;white-space:nowrap}
.topbar .wordmark{left:72px;top:34px;font-size:40px}
.nav{right:72px;top:42px;display:flex;gap:42px;font-size:27px;font-weight:700;color:var(--white)}

.hero{left:0;top:123px;width:1200px;height:717px;
  background:linear-gradient(180deg,#8fb25a 0%,#c2d68a 35%,#d9cfa4 62%,#b8946a 100%)}
.hero-kicker{left:73px;top:214px;font-size:36px;font-weight:700;color:var(--white)}
.hero-title{left:73px;top:252px;font-size:66px;font-weight:700;color:var(--white);line-height:1.1}
.pill-sm{left:73px;top:355px;width:138px;height:36px;border-radius:18px;background:var(--brand);color:var(--white);font-size:17px;font-weight:600;display:flex;align-items:center;justify-content:center}

.band{left:0;width:1200px;background:var(--band)}

.section-title{left:0;width:1200px;text-align:center;font-weight:300;font-size:100px;color:#222;line-height:1}
.rule{height:7px;background:var(--brand)}

.card{background:var(--white);box-shadow:var(--card-shadow);border-radius:6px}
.mission-card{top:1180px;width:340px;height:428px;text-align:center;padding:0 12px}
.icon-ring{width:146px;height:146px;border:2px solid var(--brand);border-radius:50%;margin:38px auto 0;display:flex;align-items:center;justify-content:center}
.card-title{color:var(--brand);font-weight:700;font-size:26px;margin-top:40px;letter-spacing:.5px}
.card-text{font-size:18px;line-height:30px;color:#555;margin-top:16px}

.btn{height:76px;border-radius:38px;background:var(--brand);color:var(--white);font-size:30px;font-weight:600;display:flex;align-items:center;justify-content:center}

.service-card{width:426px;height:537px;overflow:hidden}
.service-photo{height:278px;width:100%}
.service-body{padding:34px 30px 0 24px}
.category{font-size:19px;color:var(--muted)}
.service-title{font-size:33px;font-weight:700;color:var(--brand);margin-top:18px;line-height:1.1}
.service-text{font-size:19px;line-height:28px;color:#444;margin-top:10px}

.footer{left:0;top:3706px;width:1200px;height:695px;background:var(--brand)}
.footer-wordmark{left:82px;top:3868px;font-size:56px}
.social{top:3866px;width:73px;height:73px;background:#2f5fb3;border-radius:4px}
.footer-rule{left:0;top:4058px;width:1200px;height:2px;background:rgba(255,255,255,.45)}
.footer-links{left:88px;top:4112px;font-size:25px;font-weight:700;color:var(--white);line-height:51px;list-style:none}
.footer-contact{left:798px;top:4112px;font-size:25px;font-weight:700;color:var(--white);line-height:51px;font-style:normal}
.footer-contact .plain{font-weight:400}
</style>
</head>
<body>

<header class="abs topbar">
  <div class="abs wordmark">ANCHOR COVER</div>
  <nav class="abs nav"><span>Sevices</span><span>Help</span><span>Website</span></nav>
</header>

<section class="abs hero" role="img" aria-label="Photo of a small wooden house beside rising stacks of coins with seedlings growing from them, on a blurred green background"></section>
<div class="abs hero-kicker">ANCHOR COVER IS</div>
<div class="abs hero-title">THE ANSWER</div>
<div class="abs pill-sm">Know more</div>

<div class="abs band" style="top:840px;height:64px"></div>

<h2 class="abs section-title" style="top:984px">OUR MISSION</h2>
<div class="abs rule" style="left:0;top:1103px;width:285px"></div>
<div class="abs rule" style="left:933px;top:1103px;width:267px"></div>

<article class="abs card mission-card" style="left:88px">
  <div class="icon-ring">
    <svg width="56" height="60" viewBox="0 0 56 60"><circle cx="28" cy="14" r="11" fill="var(--brand)"/><rect x="22" y="22" width="12" height="16" fill="var(--brand)"/><rect x="8" y="38" width="40" height="10" rx="3" fill="var(--brand)"/><rect x="4" y="52" width="48" height="5" fill="var(--brand)"/></svg>
  </div>
  <h3 class="card-title">COMPLIANCE</h3>
  <p class="card-text">HR and Safety onsite compliance audits are available, as well as training and certification for all types of businesses.</p>
</article>

<article class="abs card mission-card" style="left:456px">
  <div class="icon-ring">
    <svg width="70" height="56" viewBox="0 0 70 56"><rect x="4" y="8" width="54" height="32" rx="3" fill="var(--brand)"/><rect x="12" y="16" width="38" height="16" rx="2" fill="#fff"/><circle cx="31" cy="24" r="5" fill="var(--brand)"/><ellipse cx="54" cy="44" rx="12" ry="5" fill="var(--brand)"/><rect x="42" y="44" width="24" height="8" fill="var(--brand)"/><ellipse cx="54" cy="52" rx="12" ry="4" fill="var(--brand)"/></svg>
  </div>
  <h3 class="card-title">PROFIT LEAKS</h3>
  <p class="card-text">We detect and correct the profit leaks inherent in every work comp program that drives the costs.</p>
</article>

<article class="abs card mission-card" style="left:824px">
  <div class="icon-ring">
    <svg width="56" height="64" viewBox="0 0 56 64" fill="none" stroke="var(--brand)" stroke-width="3"><path d="M8 4h30l12 12v44H8z"/><path d="M38 4v12h12"/><circle cx="19" cy="32" r="7"/><circle cx="37" cy="32" r="7"/><path d="M26 32h4"/><path d="M16 48h24M16 54h18"/></svg>
  </div>
  <h3 class="card-title">CLAIMS</h3>
  <p class="card-text">We provide employers with immediate, ongoing injury and claims management consulting.</p>
</article>

<div class="abs btn" style="left:455px;top:1693px;width:314px">Know more</div>

<div class="abs band" style="top:1801px;height:77px"></div>

<h2 class="abs section-title" style="top:1980px">OUR SERVICES</h2>
<div class="abs rule" style="left:0;top:2092px;width:285px"></div>
<div class="abs rule" style="left:963px;top:2092px;width:237px"></div>

<article class="abs card service-card" style="left:123px;top:2236px">
  <div class="service-photo" role="img" aria-label="Photo of a business team in dark suits standing in an office" style="background:linear-gradient(180deg,#9aa2a6,#3d4246)"></div>
  <div class="service-body">
    <p class="category">Category 1</p>
    <h3 class="service-title">HR Services</h3>
    <p class="service-text">We can do it all-from handbooks to managing your human resource department.</p>
  </div>
</article>

<article class="abs card service-card" style="left:663px;top:2236px">
  <div class="service-photo" role="img" aria-label="Photo of two colleagues shaking hands across a desk with a laptop" style="background:linear-gradient(135deg,#5a6770,#b8c2c6 60%,#e2e4e0)"></div>
  <div class="service-body">
    <p class="category">Category 2</p>
    <h3 class="service-title">Premium Recovery</h3>
    <p class="service-text">We perform a forensic audit, detect and correct the profit leaks, resulting in premium being refunded to you.</p>
  </div>
</article>

<article class="abs card service-card" style="left:123px;top:2887px">
  <div class="service-photo" role="img" aria-label="Photo of a businessman gesturing over a desk with papers and a laptop" style="background:linear-gradient(135deg,#2c3e5c,#8d9db4 55%,#d9dde3)"></div>
  <div class="service-body">
    <p class="category">Category 3</p>
    <h3 class="service-title">Re-Audit Services</h3>
    <p class="service-text">We will guide you through your worker's compensation audit while representing your interests.</p>
  </div>
</article>

<article class="abs card service-card" style="left:663px;top:2887px">
  <div class="service-photo" role="img" aria-label="Photo of two coworkers reviewing work together at a laptop" style="background:linear-gradient(135deg,#3e3a36,#9a8470 55%,#c9b8a3)"></div>
  <div class="service-body">
    <p class="category">Category 4</p>
    <h3 class="service-title">Safety Compliance</h3>
    <p class="service-text">We offer onsite training in English and Spanish. Discount safety equipment and drug test as low as $20 are available.</p>
  </div>
</article>

<div class="abs btn" style="left:463px;top:3497px;width:309px">View all</div>

<div class="abs band" style="top:3632px;height:74px"></div>

<footer class="abs footer"></footer>
<div class="abs wordmark footer-wordmark">ANCHOR COVER</div>
<div class="abs social" style="left:800px" aria-label="Social profile"></div>
<div class="abs social" style="left:920px" aria-label="Social profile"></div>
<div class="abs social" style="left:1040px" aria-label="Social profile"></div>
<div class="abs footer-rule"></div>
<ul class="abs footer-links">
  <li>View in browser</li>
  <li>Unsubscribe</li>
  <li>Get help</li>
  <li>Privacy policy</li>
</ul>
<address class="abs footer-contact">
  48 Harbor View Rd. Suite 5,<br>
  Milford, FL 33900<br>
  <span class="plain">info@anchorcover.com</span><br>
  555.014.2270<br>
  anchorcover.com
</address>

</body>
</html>
```